business card deign

Logo needs the following on it.
1. attached logo
2. Tagline - "If it keeps a drink cold or the party going...we do it!"
3. Name- Delia Fenwick, Founder and CPO
4. Address - 418 E. Harlow Avenue, Ste 2204, Tampa, FL. 33719
5. Phone - 720.555.0187

```html
<!DOCTYPE html>
<html lang="en">
<head>
<meta charset="utf-8">
<title>Talloway Business Card</title>
<link rel="stylesheet" href="https://fonts.googleapis.com/css2?family=Courgette&family=Montserrat:wght@400;700&family=Oswald:wght@500&display=swap">
<style>
  :root {
    --stage: #2b2b2b;
    --card-black: #050505;
    --card-white: #ffffff;
    --soft-grey: #e4e4e4;
    --silver-light: #f2f2f2;
    --silver-dark: #8a8a8a;
    --ink: #111111;
    --text-light: #ffffff;
    --text-muted: #d9d9d9;
  }
  * { margin: 0; padding: 0; box-sizing: border-box; }
  html, body { width: 1200px; height: 875px; overflow: hidden; }
  body {
    background: var(--stage);
    position: relative;
    font-family: "Montserrat", sans-serif;
  }
  .card {
    position: absolute;
    width: 525px;
    height: 300px;
    border-radius: 16px;
    overflow: hidden;
    background: var(--card-black);
    box-shadow: 0 18px 40px rgba(0,0,0,.45);
  }
  /* Back side */
  .card-back { left: 60px; top: 130px; }
  .card-back .emblem-area {
    position: absolute;
    left: 200px; top: 40px;
    width: 125px; height: 170px;
    border-radius: 10px;
    background: linear-gradient(115deg, var(--silver-light) 0%, var(--silver-light) 45%, var(--silver-dark) 100%);
  }
  .card-back .tagline {
    position: absolute;
    left: 0; right: 0; bottom: 42px;
    text-align: center;
    font-family: "Courgette", cursive;
    font-size: 19px;
    color: var(--text-light);
  }
  /* Front side */
  .card-front { left: 615px; top: 430px; }
  .card-front .light-panel {
    position: absolute;
    left: 0; top: 0; bottom: 0;
    width: 300px;
    background: var(--card-white);
    border-radius: 16px 0 0 16px;
  }
  .card-front .emblem-decor {
    position: absolute;
    left: 140px; top: 0;
    width: 215px; height: 300px;
    background: linear-gradient(180deg, var(--soft-grey) 0%, #d2d2d2 100%);
    border-radius: 0 0 24px 0;
  }
  .card-front .brand {
    position: absolute;
    left: 38px; top: 150px;
    display: flex; align-items: center; gap: 10px;
    font-family: "Oswald", sans-serif;
    font-weight: 500;
    font-size: 22px;
    letter-spacing: 6px;
    color: var(--ink);
  }
  .card-front .brand .mark {
    width: 14px; height: 14px;
    border-radius: 50%;
    background: var(--ink);
  }
  .card-front .details {
    position: absolute;
    right: 26px; top: 34px;
    text-align: right;
    color: var(--text-muted);
  }
  .details .name {
    font-weight: 700;
    font-size: 22px;
    color: var(--text-light);
    letter-spacing: .5px;
  }
  .details .role { font-size: 12px; margin-top: 2px; }
  .details .address { font-size: 11px; line-height: 1.55; margin-top: 14px; }
  .details .phone {
    margin-top: 8px;
    font-size: 14px;
    font-weight: 700;
    color: var(--text-light);
    display: flex; align-items: center; justify-content: flex-end; gap: 6px;
  }
  .phone svg { width: 13px; height: 13px; fill: var(--text-light); }
</style>
</head>
<body>
  <section class="card card-back">
    <div class="emblem-area" role="img" aria-label="Brand emblem in brushed silver"></div>
    <p class="tagline">If it keeps a drink cold or the party going...we do it!</p>
  </section>

  <section class="card card-front">
    <div class="light-panel"></div>
    <div class="emblem-decor" role="img" aria-label="Large faint brand emblem decoration"></div>
    <div class="brand"><span class="mark"></span>TALLOWAY</div>
    <div class="details">
      <h1 class="name">DELIA FENWICK</h1>
      <p class="role">Founder &amp; CEO</p>
      <p class="address">418 E. Harlow Avenue<br>Ste 2204, Tampa, FL 33719</p>
      <p class="phone">
        <svg viewBox="0 0 24 24" aria-hidden="true"><path d="M6.6 10.8a15.1 15.1 0 0 0 6.6 6.6l2.2-2.2a1 1 0 0 1 1-.25 11.4 11.4 0 0 0 3.6.57 1 1 0 0 1 1 1V20a1 1 0 0 1-1 1A17 17 0 0 1 3 4a1 1 0 0 1 1-1h3.5a1 1 0 0 1 1 1c0 1.25.2 2.45.57 3.57a1 1 0 0 1-.25 1z"/></svg>
        720.555.0187
      </p>
    </div>
  </section>
</body>
</html>
```